Business cards - KESTO Roofing & Siding

We need simple business cards made up for our Roofing & Siding business based in Calgary Alberta.
The logo on one side of the card and potentially our slogan "Raised with care, proven by seasons".
The other side could have:
-A small logo
-Rep name:
-Rep cell phone:
-Rep email:
-Office phone: 403-386-2049
-Website: PrairieShinglePros.com

We would like to incorporate the colours from our logo, especially the lite blue on the jpeg file. I have attached the ai file and jpeg file. We like the colours better on the jpeg file.

I do not require a money back guarantee

```html
<!DOCTYPE html>
<html lang="en">
<head>
<meta charset="utf-8">
<title>KESTO Roofing &amp; Siding – Business Cards</title>
<link rel="stylesheet" href="https://fonts.googleapis.com/css2?family=Lato:wght@400;700&display=swap">
<style>
  :root {
    --bg: #2b2b2d;
    --card-dark: #1c1c1e;
    --card-light: #ffffff;
    --brand-blue: #0a8bf0;
    --brand-blue-deep: #0066b3;
    --brand-red: #e5202a;
    --ink: #2a2a2a;
    --silver: #d9d9db;
  }
  * { box-sizing: border-box; margin: 0; padding: 0; }
  html, body { width: 1200px; height: 900px; overflow: hidden; }
  body {
    background: var(--bg);
    font-family: "Lato", sans-serif;
    position: relative;
  }
  .card {
    position: absolute;
    border-radius: 22px;
    overflow: hidden;
    box-shadow: 0 18px 40px rgba(0,0,0,.45);
  }

  /* Front */
  .card-front {
    left: 60px; top: 270px;
    width: 630px; height: 360px;
    background: var(--card-dark);
    display: flex; flex-direction: column;
    align-items: center; justify-content: center;
    gap: 46px;
  }
  .wordmark {
    display: flex; align-items: center; gap: 16px;
    color: var(--silver);
    font-weight: 700;
    font-size: 34px;
    letter-spacing: 3px;
  }
  .wordmark-square {
    width: 22px; height: 22px;
    background: var(--brand-blue);
  }
  .slogan {
    font-size: 21px;
    font-weight: 400;
    letter-spacing: 1.5px;
    text-transform: uppercase;
    white-space: nowrap;
  }
  .slogan-lead { color: var(--brand-blue); }
  .slogan-close { color: var(--brand-red); }

  /* Back */
  .card-back {
    left: 780px; top: 135px;
    width: 360px; height: 630px;
    background: var(--card-light);
  }
  .rep {
    position: absolute; left: 0; right: 0; top: 70px;
    text-align: center;
  }
  .rep-name {
    color: var(--brand-blue);
    font-size: 33px;
    font-weight: 400;
    letter-spacing: .5px;
  }
  .rep-title {
    color: var(--brand-red);
    font-size: 20px;
    margin-top: 4px;
  }
  .divider {
    width: 34px; height: 4px;
    background: var(--brand-blue);
    margin: 20px auto 22px;
  }
  .address {
    color: var(--ink);
    font-size: 19px;
    line-height: 1.4;
  }
  .contact-icons {
    display: flex; justify-content: center; gap: 14px;
    margin: 26px 0 20px;
  }
  .contact-icons svg { width: 18px; height: 18px; }
  .contact-list {
    list-style: none;
    color: var(--ink);
    font-size: 19px;
    line-height: 1.42;
  }
  .brand-band {
    position: absolute; left: 0; right: 0; bottom: 0;
    height: 112px;
    background: var(--brand-blue);
    display: flex; align-items: center; justify-content: center; gap: 12px;
    color: var(--card-light);
    font-size: 20px; font-weight: 700; letter-spacing: 1px;
  }
  .brand-band-square {
    width: 16px; height: 16px;
    background: var(--card-light);
  }
</style>
</head>
<body>

<section class="card card-front" aria-label="Business card front">
  <div class="wordmark">
    <span class="wordmark-square"></span>
    <span>KESTO Roofing &amp; Siding</span>
  </div>
  <p class="slogan"><span class="slogan-lead">Raised with care,</span> <span class="slogan-close">proven by seasons</span></p>
</section>

<section class="card card-back" aria-label="Business card back">
  <div class="rep">
    <h1 class="rep-name">DEREK LANGFORD</h1>
    <p class="rep-title">Managing Director</p>
    <div class="divider"></div>
    <p class="address">2284 - 9 Avenue S.E. Calgary<br>Alberta T2G 0R4</p>

    <div class="contact-icons">
      <svg viewBox="0 0 24 24" aria-label="Office phone"><path fill="var(--brand-blue)" d="M6.6 10.8a15.1 15.1 0 0 0 6.6 6.6l2.2-2.2a1 1 0 0 1 1-.25 11.4 11.4 0 0 0 3.6.57 1 1 0 0 1 1 1V20a1 1 0 0 1-1 1A17 17 0 0 1 3 4a1 1 0 0 1 1-1h3.5a1 1 0 0 1 1 1c0 1.25.2 2.45.57 3.57a1 1 0 0 1-.25 1z"/></svg>
      <svg viewBox="0 0 24 24" aria-label="Cell phone"><rect x="6" y="2" width="12" height="20" rx="2" fill="var(--brand-blue)"/><rect x="8" y="5" width="8" height="12" fill="#fff"/></svg>
      <svg viewBox="0 0 24 24" aria-label="Email"><rect x="2" y="5" width="20" height="14" rx="2" fill="var(--brand-blue)"/><path d="M3 6l9 7 9-7" stroke="#fff" stroke-width="1.6" fill="none"/></svg>
      <svg viewBox="0 0 24 24" aria-label="Website"><circle cx="12" cy="12" r="10" fill="var(--brand-blue)"/><path d="M2 12h20M12 2c3 3 3 17 0 20M12 2c-3 3-3 17 0 20" stroke="#fff" stroke-width="1.3" fill="none"/></svg>
    </div>

    <ul class="contact-list">
      <li>403-386-2049</li>
      <li>403-386-2049</li>
      <li>derek@prairieshinglepros.com</li>
      <li>PrairieShinglePros.com</li>
    </ul>
  </div>

  <div class="brand-band">
    <span class="brand-band-square"></span>
    <span>KESTO Roofing &amp; Siding</span>
  </div>
</section>

</body>
</html>
```